EPC Marketing Flyer Pinefold HC

Company Name: Pinefold Homecheck Ltd
Product: Residential EPCs
Territory: Nationwide (UK)
Marketing channel: Flyer will be used for email and postal mailshots. We have not targeted this particular segment of the market before, so we need it to be eye catching, clearly messaged and encourage the recipient to get in touch.

We need a flyer to promote our services to conduct EPCs owned by public and private sector for residential ONLY (NOT Commercial), on a large or small scale.

Our Surveyors: experienced and accredited surveyors, quality service, quick and professional

Our Business: Warm Ledger Accredited, Reputation in business for excellence, fast growing

Our Service: Friendly, high quality, quick and professional

Colours: Designs in green and white (same shade as corporate colours), with our logo, and warm ledger accreditation logo, promoting our business.

Target Market(s)

Estate Agencies, Housing Associations, Local Authorities (Housing Departments), House Builders (NOT Home Owners Directly)

Industry/Entity Type

It Company

Font styles to use
Sans Serif
Other font styles liked:
• Calibri

Colors
add136
9bcb3c
cadf82
f6faec
eaf2ce

Requirements
Must have
• Our contact number etc must be clearly visible, and that we do EPCs
• Must state: What is an EPC? An EPC (Energy Performance Certificate) gives a property an energy efficiency rating from A (most efficient) to G (least efficient) and is valid for 10 years. An EPC can also provide recommendations on home improvement measures which once complete can improve the energy efficiency of the property.
• Who needs and EPC? All landlords and home owners, as all properties available to buy or rent require a valid and current EPC.
• Contact details:
• Tel: 08000 915 462
• Website: www.pinefold-hc.co.uk
• Email: epc@pinefold-hc.co.uk
• we must also be ably to print out the flyer
Nice to have
• Nice images to accompany the text which give a feeling of Environmentally Green, Home Energy Efficiency, Home Warmth and family - see example attached. And image of survey professional at work.
Should not have
• Any reference to cost or pricing
• Warm ledger logo art work must not be any other size that that specified in guidance document attached.

```html
<!DOCTYPE html>
<html lang="en">
<head>
<meta charset="utf-8">
<title>EPC Flyer – Pinefold Homecheck Ltd</title>
<link rel="stylesheet" href="https://fonts.googleapis.com/css2?family=Oswald:wght@500;600;700&family=Lato:wght@400;700&display=swap">
<style>
  :root {
    --green-deep: #2f8a22;
    --green-main: #4ea832;
    --green-bright: #7cc242;
    --green-light: #cadf82;
    --green-pale: #eaf2ce;
    --white: #ffffff;
    --ink: #141a12;
    --grey-ring: #e9ece6;
  }
  * { margin: 0; padding: 0; box-sizing: border-box; }
  html, body { width: 875px; height: 1200px; overflow: hidden; background: #f2f2ee; }
  .flyer {
    position: relative; width: 875px; height: 1200px; overflow: hidden;
    font-family: "Lato", "Calibri", sans-serif; color: var(--white);
  }
  .flyer-backdrop { position: absolute; inset: 0; }
  .headline {
    position: absolute; left: 32px; top: 48px; width: 520px;
    font-family: "Oswald", sans-serif; font-weight: 700; text-transform: uppercase;
    line-height: 1.3; letter-spacing: 0; white-space: nowrap;
  }
  .headline .dark { color: var(--ink); font-size: 44px; display: block; }
  .headline .light { color: var(--white); font-size: 36px; display: block; }
  .info { position: absolute; left: 32px; top: 258px; width: 510px; }
  .info h2 {
    font-family: "Oswald", sans-serif; font-weight: 500; font-size: 23px;
    color: var(--ink); margin-bottom: 4px; line-height: 1.25;
  }
  .info p { font-size: 17.5px; line-height: 1.4; margin-bottom: 18px; }
  .info .surveyors p { font-size: 16.5px; }
  .contact { position: absolute; left: 32px; top: 805px; width: 700px; }
  .contact h2 {
    font-family: "Oswald", sans-serif; font-weight: 500; font-size: 25px;
    color: var(--ink); margin-bottom: 12px;
  }
  .contact-grid { display: grid; grid-template-columns: 320px 1fr; row-gap: 10px; font-size: 18px; }
  .contact-grid b { color: var(--ink); font-weight: 700; }
  .photo { position: absolute; }
  .photo-home {
    left: 555px; top: 50px; width: 350px; height: 350px; border-radius: 50%;
    background: linear-gradient(160deg, #f4e9a8 0%, #bcd675 40%, #4f8a2a 100%);
    border: 14px solid var(--white); box-shadow: 0 0 0 4px var(--grey-ring);
  }
  .photo-family {
    left: 0; top: 945px; width: 560px; height: 255px;
    background: linear-gradient(180deg, rgba(216,195,165,0) 0%, #d8c3a5 25%, #b79c7c 62%, #5c9b2e 88%, #3f7f22 100%);
    border-top-right-radius: 120px;
  }
  .energy-rating {
    position: absolute; left: 555px; top: 440px; width: 360px; height: 360px; border-radius: 50%;
    background: var(--white); box-shadow: 0 0 0 4px var(--grey-ring);
  }
  .energy-rating svg { position: absolute; left: 0; top: 0; }
  .brand {
    position: absolute; right: 40px; top: 1080px;
    display: flex; align-items: center; gap: 12px;
  }
  .brand-dot { width: 40px; height: 40px; border-radius: 50%; background: var(--green-main); }
  .brand-name {
    font-family: "Lato", sans-serif; font-weight: 700; font-size: 28px; color: var(--green-main);
  }
  .accreditation-badge {
    position: absolute; left: 770px; top: 950px; width: 78px; height: 78px;
    background: var(--green-deep); border-radius: 6px;
  }
</style>
</head>
<body>
<div class="flyer">
  <svg class="flyer-backdrop" width="875" height="1200" viewBox="0 0 875 1200">
    <defs>
      <linearGradient id="fieldGreen" x1="0" y1="0" x2="1" y2="1">
        <stop offset="0" stop-color="#3e9a2a"/>
        <stop offset="0.55" stop-color="#5cb236"/>
        <stop offset="1" stop-color="#8cc84a"/>
      </linearGradient>
      <linearGradient id="paleSweep" x1="0" y1="0" x2="1" y2="0">
        <stop offset="0" stop-color="#f6faec"/>
        <stop offset="1" stop-color="#ffffff"/>
      </linearGradient>
    </defs>
    <rect width="875" height="1200" fill="url(#fieldGreen)"/>
    <path d="M300 1200 C520 1080 760 960 875 820 V1200 Z" fill="#9bcb3c"/>
    <path d="M380 1200 C580 1100 780 990 875 880 V1200 Z" fill="#cadf82"/>
    <path d="M430 1200 C620 1120 800 1020 875 930 V1200 Z" fill="url(#paleSweep)"/>
  </svg>

  <h1 class="headline">
    <span class="dark">Warm Ledger Accredited,</span>
    <span class="dark">Reputation in Business</span>
    <span class="light">For Excellence, Fast Growing</span>
  </h1>

  <div class="photo photo-home" role="img" aria-label="Photo of a small house covered in grass, in a meadow of daisies"></div>

  <div class="energy-rating">
    <svg width="360" height="360" viewBox="0 0 360 360" role="img" aria-label="Energy efficiency rating scale from A to G">
      <text x="0" y="0" transform="translate(62 245) rotate(-90)" font-family="Oswald, sans-serif" font-weight="700" font-size="26" fill="#2f8a22">ENERGY</text>
      <text x="0" y="0" transform="translate(86 245) rotate(-90)" font-family="Oswald, sans-serif" font-weight="700" font-size="26" fill="#2f8a22">EFFICIENCY</text>
      <g font-family="Oswald, sans-serif" font-weight="700" font-size="20" fill="#fff">
        <path d="M92 36 h28 l12 12 l-12 12 h-28 Z" fill="#1f9a3a"/><text x="98" y="56">A</text>
        <path d="M92 64 h48 l12 12 l-12 12 h-48 Z" fill="#4fb041"/><text x="118" y="84">B</text>
        <path d="M92 92 h68 l12 12 l-12 12 h-68 Z" fill="#97c93c"/><text x="138" y="112">C</text>
        <path d="M92 120 h88 l12 12 l-12 12 h-88 Z" fill="#e5e22a"/><text x="158" y="140">D</text>
        <path d="M92 148 h108 l12 12 l-12 12 h-108 Z" fill="#f6b520"/><text x="178" y="168">E</text>
        <path d="M92 176 h128 l12 12 l-12 12 h-128 Z" fill="#ee7a22"/><text x="198" y="196">F</text>
        <path d="M92 206 h148 l14 14 l-14 14 h-148 Z" fill="#e02626"/><text x="218" y="228">G</text>
      </g>
    </svg>
  </div>

  <section class="info">
    <div class="info-block">
      <h2>What is an EPC?</h2>
      <p>An EPC (Energy Performance Certificate) gives a property an energy efficiency rating from A (most efficient) to G (least efficient) and is valid for 10 years. An EPC can also provide recommendations on home improvement measures which once complete can improve the energy efficiency of the property.</p>
    </div>
    <div class="info-block">
      <h2>Who needs and EPC?</h2>
      <p>All landlords and home owners, as all properties available to buy or rent require a valid and current EPC.</p>
    </div>
    <div class="info-block">
      <h2>Our Service:</h2>
      <p>Friendly, high quality, quick and professional Service</p>
    </div>
    <div class="info-block surveyors">
      <h2>Our Surveyors:</h2>
      <p>experienced and accredited surveyors, quality service, quick and professional</p>
    </div>
  </section>

  <section class="contact">
    <h2>Contact Details:</h2>
    <div class="contact-grid">
      <span><b>Telephone:</b> 08000 915 462</span>
      <span><b>Email:</b> epc@pinefold-hc.co.uk</span>
      <span></span>
      <span><b>Website:</b> www.pinefold-hc.co.uk</span>
    </div>
  </section>

  <div class="photo photo-family" role="img" aria-label="Photo of a smiling family of four lying together on green grass"></div>

  <div class="accreditation-badge" role="img" aria-label="Accreditation badge"></div>

  <div class="brand">
    <span class="brand-dot"></span>
    <span class="brand-name">Pinefold Homecheck Ltd</span>
  </div>
</div>
</body>
</html>
```